Veltrionix Knowledge Enhancement Company Website

Veltrionix is knowledge enhancement Highend and Deep Technology Company who has training programs in Applied Quantum, Applied Artificial Intelligence and Data Science. All the technologies are very advanced and future technologies and the website should reflect the technology advancement. Looking for a sophisticated web design which will reflect our focus on deep and future technologies. Logo file is uploaded

Target Market(s)

Big Corporates and Premium Colleges

Industry/Entity Type

Technology, Deep Technology, Future Technology

Coding

Coded - Design and coding required

Number of Pages Required

5+ page

Requirements
Must have
• A Very Contemporary clean look and should reflect Future Technologies
Nice to have
• Should be very Classy
Should not have
• Traditional Fonts and Colors

```html
<!DOCTYPE html>
<html lang="en">
<head>
<meta charset="utf-8">
<title>Veltrionix</title>
<link rel="stylesheet" href="https://fonts.googleapis.com/css2?family=Cinzel:wght@600;700;800&family=Lato:wght@300;400;700&family=Poppins:wght@500;600;800&display=swap">
<style>
:root{
  --blue:#29a9e1;
  --blue-deep:#0b5fd0;
  --navy:#0a3f9e;
  --ink:#111111;
  --text:#3a3a3a;
  --pale:#eaf5fc;
  --white:#ffffff;
  --black:#000000;
  --line:#cfcfcf;
}
*{margin:0;padding:0;box-sizing:border-box}
html,body{width:1200px;height:3198px;overflow:hidden}
body{position:relative;background:var(--white);font-family:'Lato',sans-serif;color:var(--text)}
.abs{position:absolute}
.cinzel{font-family:'Cinzel',serif;font-weight:700}

/* header */
.topbar{left:0;top:0;width:1200px;height:104px;background:var(--white)}
.brand{left:100px;top:30px;display:flex;align-items:center;gap:10px}
.brand-mark{width:34px;height:34px;background:var(--blue)}
.brand-name{font-family:'Cinzel',serif;font-weight:700;font-size:26px;color:var(--blue)}
.contact-item{top:30px;display:flex;gap:10px;align-items:flex-start}
.contact-icon{width:32px;height:32px;border-radius:50%;background:var(--blue);display:flex;align-items:center;justify-content:center}
.contact-item .label{font-family:'Cinzel',serif;font-weight:700;font-size:13px;color:var(--ink)}
.contact-item .value{font-family:'Cinzel',serif;font-weight:700;font-size:15px;color:var(--ink);margin-top:4px}

/* hero */
.hero{left:0;top:104px;width:1200px;height:509px;background:radial-gradient(ellipse at 50% 60%,#2f8fe8 0%,#0f63d6 45%,#0a46b3 100%)}
.hero-art{left:0;top:0;width:1200px;height:509px;background:linear-gradient(160deg,rgba(255,255,255,0) 55%,rgba(220,235,250,.55) 85%,#f3f6fa 100%)}
.nav{left:112px;top:0;width:976px;height:64px;background:rgba(9,45,140,.85);border-radius:0 0 12px 12px;display:flex;align-items:center;padding:0 18px;gap:0}
.nav a{font-family:'Cinzel',serif;font-weight:700;font-size:15px;color:var(--white);text-decoration:none;margin-right:57px}
.nav a.active{text-decoration:underline}
.nav .search{margin-left:auto;width:26px;height:26px;border-radius:50%;background:var(--white);display:flex;align-items:center;justify-content:center}
.hero-kicker{left:0;top:153px;width:1200px;text-align:center;font-size:22px;color:var(--white)}
.hero-title{left:0;top:185px;width:1200px;text-align:center;font-size:52px;color:var(--white);letter-spacing:.5px}
.hero-sub{left:290px;top:258px;width:620px;text-align:center;font-size:15px;font-weight:700;color:var(--white);line-height:25px}
.btn-start{left:497px;top:326px;width:206px;height:67px;background:var(--white);border-radius:0 30px 0 30px;display:flex;align-items:center;justify-content:center;font-family:'Cinzel',serif;font-weight:700;font-size:20px;color:var(--ink)}

/* about */
.about{left:0;top:613px;width:1200px;height:485px;background:linear-gradient(90deg,#f4f6f9,#ffffff 60%)}
.about-ring{left:115px;top:72px;width:412px;height:412px;border-radius:50%;border:2px solid var(--blue)}
.about-photo{left:112px;top:75px;width:396px;height:396px;border-radius:50%;background:radial-gradient(circle at 45% 40%,#5a7fc0,#1d3f8a 60%,#0b1f52)}
.about-title{left:584px;top:68px;font-size:40px;color:var(--ink)}
.about-title span{color:var(--blue)}
.about-text{left:584px;top:120px;width:510px;font-size:15px;line-height:26px;font-weight:300;color:var(--ink)}
.btn-read{left:583px;top:420px;width:205px;height:68px;background:var(--blue);border-radius:0 30px 0 30px;display:flex;align-items:center;justify-content:center;font-family:'Cinzel',serif;font-weight:700;font-size:20px;color:var(--white);box-shadow:3px 4px 8px rgba(0,0,0,.15)}

/* programmes */
.programs{left:0;top:1167px;width:1200px;height:644px;background:linear-gradient(180deg,#2aa8e2,#2eb0e6)}
.programs-title{left:0;top:56px;width:1200px;text-align:center;font-size:42px;color:var(--white)}
.program-card{top:155px;width:402px;height:402px;border-radius:50%;overflow:hidden;border:2px solid var(--white)}
.program-photo{width:100%;height:100%}
.program-cap{position:absolute;left:50%;bottom:-150px;transform:translateX(-50%);width:330px;height:250px;border-radius:50%;background:var(--white)}
.program-label{position:absolute;left:0;bottom:34px;width:100%;text-align:center;font-family:'Cinzel',serif;font-weight:700;font-size:18px;line-height:27px;color:var(--ink)}

/* numbers */
.pride-title{left:0;top:1857px;width:1200px;text-align:center;font-size:40px;color:var(--ink)}
.pride-title span{color:var(--blue)}
.stat{top:1955px;width:220px;text-align:center}
.stat .num{font-family:'Poppins',sans-serif;font-weight:800;font-size:50px;color:var(--blue);line-height:60px}
.stat .cap{font-family:'Poppins',sans-serif;font-weight:500;font-size:16px;line-height:26px;color:var(--ink);margin-top:6px}
.divider{top:1938px;width:2px;height:172px;background:var(--line)}
.divider::after{content:"";position:absolute;left:-5px;top:80px;width:12px;height:12px;border-radius:50%;background:var(--blue)}

/* contact */
.contact{left:0;top:2185px;width:1200px;height:530px;background:var(--pale)}
.contact-title{left:114px;top:78px;font-size:40px;color:var(--ink)}
.contact-title span{color:var(--blue)}
.contact-text{left:111px;top:128px;width:410px;font-size:15px;line-height:26px;font-weight:300;color:var(--ink)}
.contact-line{left:114px;display:flex;gap:14px;align-items:flex-start;font-size:17px;line-height:26px;color:var(--ink)}
.form-card{left:579px;top:68px;width:509px;height:374px;background:var(--white);box-shadow:0 2px 10px rgba(0,0,0,.06)}
.form-title{left:0;top:32px;width:100%;text-align:center;font-size:32px;color:var(--ink)}
.field{border:1px solid #cfcfcf;border-radius:3px;font-size:11px;font-weight:700;color:#333;padding:16px 14px}
.btn-submit{left:32px;top:285px;width:443px;height:55px;background:var(--blue);border-radius:0 30px 0 30px;display:flex;align-items:center;justify-content:center;font-family:'Cinzel',serif;font-weight:700;font-size:21px;color:var(--white)}

/* footer */
.footer{left:0;top:2715px;width:1200px;height:483px;background:var(--black)}
.footer-brand{left:0;top:120px;width:1200px;display:flex;justify-content:center;align-items:center;gap:16px}
.footer-brand .brand-mark{width:60px;height:60px}
.footer-brand .brand-name{font-size:48px}
.socials{left:0;top:296px;width:1200px;display:flex;justify-content:center;gap:26px}
.socials span{width:32px;height:32px;border-radius:50%;background:var(--blue)}
.footer-nav{left:0;top:372px;width:1200px;display:flex;justify-content:center;gap:57px}
.footer-nav a{font-family:'Cinzel',serif;font-weight:700;font-size:15px;color:var(--white);text-decoration:none}
.copyright{left:0;top:427px;width:1200px;text-align:center;font-family:'Cinzel',serif;font-weight:700;font-size:12px;color:var(--white)}
</style>
</head>
<body>

<header class="abs topbar">
  <div class="abs brand"><span class="brand-mark"></span><span class="brand-name">Veltrionix</span></div>
  <div class="abs contact-item" style="left:371px">
    <span class="contact-icon"><svg width="16" height="16" viewBox="0 0 24 24"><path fill="#fff" d="M6.6 10.8a15 15 0 0 0 6.6 6.6l2.2-2.2c.3-.3.7-.4 1-.2 1.1.4 2.3.6 3.6.6.6 0 1 .4 1 1V20c0 .6-.4 1-1 1A17 17 0 0 1 3 4c0-.6.4-1 1-1h3.5c.6 0 1 .4 1 1 0 1.3.2 2.5.6 3.6.1.3 0 .7-.2 1z"/></svg></span>
    <div><div class="label">Call Now:</div><div class="value">+1 555 014 2290</div></div>
  </div>
  <div class="abs contact-item" style="left:561px">
    <span class="contact-icon"><svg width="16" height="16" viewBox="0 0 24 24"><path fill="#fff" d="M3 6h18v12H3z"/><path fill="none" stroke="#29a9e1" stroke-width="2" d="M3 6l9 7 9-7"/></svg></span>
    <div><div class="label">Mail:</div><div class="value">info@veltrionix.com</div></div>
  </div>
  <div class="abs contact-item" style="left:809px">
    <span class="contact-icon"><svg width="16" height="16" viewBox="0 0 24 24"><path fill="#fff" d="M12 2a7 7 0 0 0-7 7c0 5 7 13 7 13s7-8 7-13a7 7 0 0 0-7-7zm0 9.5A2.5 2.5 0 1 1 12 6.5a2.5 2.5 0 0 1 0 5z"/></svg></span>
    <div><div class="label">Location:</div><div class="value">Veltrionix, United States</div></div>
  </div>
</header>

<section class="abs hero">
  <div class="abs hero-art" role="img" aria-label="Digital data landscape in glowing blue tones"></div>
  <nav class="abs nav">
    <a class="active" href="#">Home</a><a href="#">About</a><a href="#">Solutions</a><a href="#">Research</a><a href="#">Calculators</a><a href="#">Careers</a><a href="#" style="margin-right:0">Contact Us</a>
    <span class="search"><svg width="12" height="12" viewBox="0 0 24 24"><circle cx="10" cy="10" r="6" fill="none" stroke="#0a3f9e" stroke-width="3"/><path d="M15 15l6 6" stroke="#0a3f9e" stroke-width="3"/></svg></span>
  </nav>
  <div class="abs hero-kicker cinzel">Welcome to Veltrionix</div>
  <h1 class="abs hero-title cinzel">The Workforce Of The Future</h1>
  <p class="abs hero-sub">Corvantis Labs Academy is an essential part of Corvantis Labs, brought to life to educate the future of our workforce, both students and professionals.</p>
  <div class="abs btn-start">Get Started</div>
</section>

<section class="abs about">
  <div class="abs about-ring"></div>
  <div class="abs about-photo" role="img" aria-label="Engineer working with holographic data screens"></div>
  <h2 class="abs about-title cinzel">About <span>Veltrionix</span></h2>
  <div class="abs about-text">
    <p>We have a vision to create a quantum future by using quantum principles for engineering solutions to extremely complex problems in computing, communications, sensing, chemistry, cryptography, imaging &amp; mechanics. Our work is progressing in the direction to provide the world its first Quantum Internet and as a result create a completely secure internet and communication at immense speed and security.</p>
    <p style="margin-top:42px">We have put together a world class team of research quantum and networking scientists to build this new paradigm of secure communications for commercial customers.</p>
  </div>
  <div class="abs btn-read">Read More</div>
</section>

<section class="abs programs" role="region" aria-label="Programmes">
  <h2 class="abs programs-title cinzel">Veltrionix</h2>
  <div class="abs program-card" style="left:147px">
    <div class="program-photo" role="img" aria-label="Night city skyline under a glowing network globe" style="background:radial-gradient(circle at 50% 35%,#2f6fa8,#123a66 55%,#081c38)"></div>
    <div class="program-cap"></div>
    <div class="program-label">Build<br>Your Advantage</div>
  </div>
  <div class="abs program-card" style="left:688px">
    <div class="program-photo" role="img" aria-label="Circuit lines and a digital globe in violet and blue" style="background:radial-gradient(circle at 65% 40%,#5b4fd6,#2a2d9a 55%,#141860)"></div>
    <div class="program-cap"></div>
    <div class="program-label">The Best<br>Training Grounds</div>
  </div>
</section>

<h2 class="abs pride-title cinzel">We Take Pride <span>In Our Numbers</span></h2>
<div class="abs stat" style="left:67px"><div class="num">5+</div><div class="cap">Global Research<br>Labs</div></div>
<div class="abs divider" style="left:306px"></div>
<div class="abs stat" style="left:330px"><div class="num">25</div><div class="cap">Our Quantum<br>Scientists</div></div>
<div class="abs divider" style="left:580px"></div>
<div class="abs stat" style="left:604px"><div class="num">2</div><div class="cap">Countries World<br>Wide</div></div>
<div class="abs divider" style="left:847px"></div>
<div class="abs stat" style="left:860px"><div class="num">5+</div><div class="cap">IPs Owned</div></div>

<section class="abs contact">
  <h2 class="abs contact-title cinzel">Contact <span>Us</span></h2>
  <p class="abs contact-text">Our Vision is to provide the world its first Quantum Communication and Quantum Computing based solution by creating a completely secure internet and communication at immense speed and security. Corvantis Labs Academy is an essential part of Corvantis Labs, brought to life to educate the future of our workforce, both students and professionals.</p>
  <div class="abs contact-line" style="top:290px"><svg width="20" height="24" viewBox="0 0 24 24"><path fill="#29a9e1" d="M12 2a7 7 0 0 0-7 7c0 5 7 13 7 13s7-8 7-13a7 7 0 0 0-7-7zm0 9.5A2.5 2.5 0 1 1 12 6.5a2.5 2.5 0 0 1 0 5z"/></svg><span>Veltrionix<br>United States</span></div>
  <div class="abs contact-line" style="top:357px"><svg width="20" height="22" viewBox="0 0 24 24"><path fill="#29a9e1" d="M2 6h20v12H2z"/><path fill="none" stroke="#eaf5fc" stroke-width="2" d="M2 6l10 7 10-7"/></svg><span>info@veltrionix.com</span></div>
  <div class="abs contact-line" style="top:400px"><svg width="20" height="22" viewBox="0 0 24 24"><path fill="#29a9e1" d="M6.6 10.8a15 15 0 0 0 6.6 6.6l2.2-2.2c.3-.3.7-.4 1-.2 1.1.4 2.3.6 3.6.6.6 0 1 .4 1 1V20c0 .6-.4 1-1 1A17 17 0 0 1 3 4c0-.6.4-1 1-1h3.5c.6 0 1 .4 1 1 0 1.3.2 2.5.6 3.6.1.3 0 .7-.2 1z"/></svg><span>+1 555 014 2290</span></div>

  <div class="abs form-card">
    <h3 class="abs form-title cinzel">Get In Touch</h3>
    <div class="abs field" style="left:31px;top:90px;width:212px;height:48px">Name*</div>
    <div class="abs field" style="left:31px;top:150px;width:212px;height:48px">Email*</div>
    <div class="abs field" style="left:31px;top:211px;width:212px;height:48px">Phone*</div>
    <div class="abs field" style="left:258px;top:90px;width:218px;height:169px">Message*</div>
    <div class="abs btn-submit">Submit</div>
  </div>
</section>

<footer class="abs footer">
  <div class="abs footer-brand"><span class="brand-mark"></span><span class="brand-name">Veltrionix</span></div>
  <div class="abs socials" aria-label="Social links"><span></span><span></span><span></span><span></span></div>
  <nav class="abs footer-nav"><a href="#">Home</a><a href="#">About</a><a href="#">Solutions</a><a href="#">Research</a><a href="#">Calculators</a><a href="#">Careers</a><a href="#">Contact Us</a></nav>
  <div class="abs copyright">Copyrights@2023.Veltrionix.All Rights Reserved</div>
</footer>

</body>
</html>
```